Harbor Mortgage Relief

Please help us give our website a remake or a FACELIFT. It is not very good but it says what we need it to say. But the design is terrible.
I would like our new design font and logo to be used as the theme.

I also want more photos on the site.

I also want consistency with the pages so they look clean.

We want the professionals to do this, let's see what you got!

Thank you!
Updates

Project Deadline Extended
Reason: I can understand you want to be paid. So I will commit to the fee but I want you to have time to make a KICK ASS website for me dudes! Thanks

HI!  Just wanted to say thanks for your time on these.  A lot are great.  However the firefighters have nothing to do with Foreclosure.  We are saving peoples homes from the bank taking them and selling them.   I LOVE the house photos and the families on the website.  That is the direction we like.  THanks.

THANK U ALL FOR THE WORK!   I like a few ending in the numbers: 147  733  693  536  620  478  727  508     I will go over them and choose one soon.  Thank you.   You will be paid shortly. 

Requirements
Must have
• Bright, Upbeat photos. Color scheme should be in order. We like icons on the bottom. not just text.

```html
<!DOCTYPE html>
<html lang="en">
<head>
<meta charset="utf-8">
<title>Harbor Mortgage Relief</title>
<link href="https://fonts.googleapis.com/css2?family=Arimo:wght@400;700&family=Cinzel:wght@400;700&family=Roboto+Condensed:wght@400;700&family=Tinos:ital,wght@0,400;1,400&display=swap" rel="stylesheet">
<style>
:root{
  --red:#e8313a;
  --red-dark:#c8232b;
  --blue:#1a8fd8;
  --navy:#0c2c52;
  --navy-deep:#071d38;
  --page:#e6e7e8;
  --white:#ffffff;
  --ink:#3d3d3d;
  --muted:#6b6b6b;
  --nav:#3a3a3a;
  --sky:#5f9fe0;
  --grass:#4f9a2e;
}
*{margin:0;padding:0;box-sizing:border-box}
html,body{width:815px;height:1200px;overflow:hidden}
body{position:relative;background:var(--page);font-family:"Arimo",Arial,sans-serif;color:var(--ink)}
.abs{position:absolute}
.header{left:0;top:0;width:815px;height:147px;background:var(--white)}
.utility{left:621px;top:0;width:88px;height:19px;background:#e3e3e3;font-size:8px;color:#666;text-align:center;line-height:19px}
.brand{left:116px;top:34px;display:flex;align-items:center;gap:10px}
.brand-mark{width:56px;height:56px;border-radius:50%;background:var(--red)}
.brand-name{font-family:"Roboto Condensed",sans-serif;font-weight:700;font-size:20px;line-height:19px;color:var(--red);text-transform:uppercase;width:160px}
.call{left:423px;top:62px;font-size:13px;color:#555;display:flex;align-items:baseline;gap:7px}
.call strong{font-family:"Tinos",serif;font-weight:400;font-size:30px;color:var(--blue)}
.nav{left:105px;top:105px;width:604px;height:31px;background:linear-gradient(#555,#2e2e2e);border-radius:2px;display:flex;align-items:center}
.nav-home{width:74px;height:31px;background:#2a2a2a;display:flex;align-items:center;justify-content:center}
.nav a{font-family:"Roboto Condensed",sans-serif;font-weight:700;font-size:13px;color:#eee;text-decoration:none;padding:0 13px;height:31px;line-height:31px;border-left:1px solid #555}
.search{left:578px;top:111px;width:123px;height:19px;background:var(--white);font-size:9px;color:#999;padding-left:6px;line-height:19px}
.search-btn{left:681px;top:111px;width:19px;height:19px;background:var(--red)}
.hero{left:105px;top:147px;width:605px;height:254px;border-radius:0 0 6px 6px;overflow:hidden;background:linear-gradient(160deg,#2f6fc8 0%,#5b95de 35%,#3f5f8f 65%,#2a2f3c 100%)}
.consult{left:510px;top:147px;width:200px;height:254px;background:rgba(20,40,70,.72)}
.consult-head{height:36px;background:var(--red);color:var(--white);font-family:"Roboto Condensed",sans-serif;font-weight:700;font-size:14.5px;line-height:36px;text-align:center}
.consult p{color:var(--white);font-size:11px;line-height:12.5px;padding:10px 16px 0}
.field{position:absolute;left:16px;width:174px;height:23px;background:var(--white);border-radius:2px;font-size:8.5px;color:#777;line-height:23px;padding-left:10px}
.field em{color:var(--red);font-style:normal}
.field-select{right:0}
.send{position:absolute;left:16px;top:200px;width:172px;height:33px;background:linear-gradient(#5a6470,#3e4650);color:#9fd7ff;font-family:"Tinos",serif;font-size:18px;letter-spacing:.5px;text-align:center;line-height:33px}
.photo{background:linear-gradient(180deg,var(--sky) 0%,#b9d8f3 48%,#d9d3b8 55%,var(--grass) 72%,#2f7a1c 100%)}
.photo.beach{background:linear-gradient(180deg,#4d93e0 0%,#a8cff3 55%,#f3f3f0 75%,#e0e5ea 100%)}
.feature-text{font-size:10.5px;line-height:15.5px;color:#444;width:132px}
.btn{background:var(--red);color:var(--white);font-family:"Tinos",serif;font-size:12.5px;text-align:center;line-height:25px;height:25px;width:107px}
.news-title{left:559px;top:419px;font-family:"Cinzel",serif;font-size:20px;color:var(--red);width:160px;border-bottom:1px solid #ccc;padding-bottom:2px}
.news{left:547px;top:451px;list-style:none;font-size:8.7px;color:#444;line-height:16.8px}
.news li::before{content:"»";color:var(--red);margin-right:5px}
.about-title{left:108px;top:656px;font-family:"Cinzel",serif;font-size:22px;color:var(--red);letter-spacing:.5px}
.about-text{left:108px;top:684px;width:420px;font-size:13px;line-height:19px;letter-spacing:.3px;color:#444}
.about-text span{color:var(--red)}
.readmore{left:108px;top:773px;width:81px;height:27px;border:1px solid #ccc;background:#f2f2f2;font-family:"Tinos",serif;font-size:12px;color:#666;text-align:center;line-height:26px}
.testimonial{left:108px;top:825px;width:403px;height:123px;background:var(--white);border:1px solid #d6d6d6;border-radius:5px}
.testimonial h3{font-family:"Cinzel",serif;font-weight:400;font-size:21px;color:var(--red);text-align:center;margin-top:13px}
.testimonial blockquote{position:absolute;left:43px;top:42px;width:345px;font-family:"Tinos",serif;font-style:italic;font-size:12.5px;line-height:18px;color:#555}
.quote-mark{font-family:"Tinos",serif;font-size:36px;color:#888;line-height:1}
.testimonial cite{position:absolute;left:42px;top:93px;font-style:normal;font-size:9px;color:#555}
.testimonial .more{position:absolute;left:309px;top:106px;font-family:"Tinos",serif;font-size:9.5px;color:var(--red)}
.video{width:148px;height:94px}
.video-bar{position:absolute;left:0;bottom:0;width:148px;height:5px;background:#333}
.video-play{position:absolute;left:64px;top:35px;width:20px;height:20px;border-radius:50%;background:rgba(255,255,255,.7)}
.footer{left:0;top:985px;width:815px;height:215px;background:radial-gradient(ellipse at 50% 0%,#1f5694 0%,var(--navy) 45%,var(--navy-deep) 100%)}
.fcol{top:1027px}
.fcol h4{font-size:13px;color:#3ea3ee;margin-bottom:5px}
.fcol li{list-style:none;font-size:8px;color:#e6eef7;line-height:13px}
.newsletter{left:379px;top:1027px;font-size:13px;font-weight:700;color:var(--white)}
.nl-input{left:377px;top:1054px;width:150px;height:23px;background:var(--white);border-radius:3px;font-size:9.5px;color:#777;line-height:23px;padding-left:9px}
.nl-btn{left:535px;top:1054px;width:75px;height:23px;background:var(--red);border-radius:3px;color:var(--white);font-weight:700;font-size:11.5px;text-align:center;line-height:23px}
.social{top:1055px;width:20px;height:20px;background:#dfe3e8;border-radius:3px}
.divider{left:0;top:1131px;width:815px;height:1px;background:#1e4170}
.legal{left:119px;top:1149px;font-size:8px;color:#e6eef7}
.copy{left:119px;top:1162px;font-size:8px;color:#3ea3ee}
</style>
</head>
<body>
<header class="abs header"></header>
<div class="abs utility">Login &nbsp;|&nbsp; Contacts</div>
<div class="abs brand"><div class="brand-mark"></div><div class="brand-name">Harbor Mortgage Relief</div></div>
<div class="abs call">Call Toll-Free Now <strong>800-555-0142</strong></div>
<nav class="abs nav">
  <div class="nav-home"><svg width="16" height="14" viewBox="0 0 16 14"><path d="M8 0 0 7h2v7h4V9h4v5h4V7h2z" fill="#fff"/></svg></div>
  <a>ABOUT US</a><a>SERVICES</a><a>FINANCING OPTIONS</a><a>CONTACT US</a>
</nav>
<div class="abs search">Search...</div>
<div class="abs search-btn"><svg width="19" height="19" viewBox="0 0 19 19"><circle cx="8" cy="8" r="4" stroke="#fff" stroke-width="2" fill="none"/><path d="M11 11l4 4" stroke="#fff" stroke-width="2"/></svg></div>

<div class="abs hero" role="img" aria-label="Smiling family of five outdoors in front of their home under a blue sky"></div>
<form class="abs consult">
  <div class="consult-head">GET A FREE CONSULTATION</div>
  <p>Please fill out this form, and we´ll call you as soon as possible.</p>
  <div class="field" style="top:82px">Name <em>*</em></div>
  <div class="field" style="top:109px">Email <em>*</em></div>
  <div class="field" style="top:136px">Phone <em>*</em></div>
  <div class="field" style="top:164px">State property is <em>*</em>
    <svg class="abs field-select" style="top:2px;right:2px" width="18" height="19" viewBox="0 0 18 19"><rect width="18" height="19" rx="2" fill="#1a8fd8"/><path d="M5 7l4 5 4-5" stroke="#fff" stroke-width="2" fill="none"/></svg>
  </div>
  <div class="send">SEND REQUEST</div>
</form>

<div class="abs photo" style="left:105px;top:423px;width:136px;height:90px" role="img" aria-label="Family standing on the lawn in front of a house"></div>
<div class="abs photo beach" style="left:247px;top:423px;width:135px;height:90px" role="img" aria-label="Parents and children laughing together under a bright sky"></div>
<div class="abs photo" style="left:387px;top:423px;width:129px;height:90px" role="img" aria-label="Couple and child relaxing on the grass beside their home"></div>
<p class="abs feature-text" style="left:108px;top:531px">Nulla venenatis. In pede mi, aliquet sit amet, euismod in, auctor ut, ligula.</p>
<p class="abs feature-text" style="left:249px;top:531px">Nulla venenatis. In pede mi, aliquet sit amet, euismod in, auctor ut, ligula.</p>
<p class="abs feature-text" style="left:392px;top:531px">Nulla venenatis. In pede mi, aliquet sit amet, euismod in, auctor ut, ligula.</p>
<div class="abs btn" style="left:108px;top:595px">LEARN MORE</div>
<div class="abs btn" style="left:249px;top:595px">LEARN MORE</div>
<div class="abs btn" style="left:391px;top:595px">LEARN MORE</div>

<h2 class="abs news-title">Latest News</h2>
<ul class="abs news">
  <li>Aliquam dapibus tincidunt metus ..</li>
  <li>Praesent justo dolor sagittis euismod..</li>
  <li>Vestibulum sed ante</li>
  <li>Donec sagittis euismod purus</li>
  <li>Praesent justo dolor sagittis ...</li>
  <li>Aliquam dapibus tincidunt metus ..</li>
  <li>Praesent justo dolor sagittis euismod..</li>
  <li>Vestibulum sed ante</li>
</ul>
<div class="abs btn" style="left:556px;top:595px">See More &nbsp;»</div>

<h2 class="abs about-title">About Harbor Mortgage Relief</h2>
<p class="abs about-text">Aliquam congue fermentum nisl. Mauris accumsan nulla vel diam. Sed in lacus ut enim <span>adipiscing</span> aliquet. &nbsp;Nulla venenatis. In pede mi, aliquet sit amet, euismod in, auctor ut, ligula. Aliquam dapibus tincidunt metus. Praesent justo dolor.</p>
<div class="abs readmore">Read More</div>

<section class="abs testimonial">
  <h3>Testimonial</h3>
  <span class="abs quote-mark" style="left:17px;top:30px">“</span>
  <blockquote>Nulla venenatis. In pede mi, aliquet sit amet, euismod in, auctor ut, ligula. Aliquam dapibus tincidunt metus. Praesent justo dolor.</blockquote>
  <span class="abs quote-mark" style="left:365px;top:64px">”</span>
  <cite>--Daniel Marsh Home Owner, NH</cite>
  <span class="more">MORE »</span>
</section>

<div class="abs video photo" style="left:554px;top:646px" role="img" aria-label="Video still of a family in front of their house"><div class="video-play"></div><div class="video-bar"></div></div>
<div class="abs video photo beach" style="left:554px;top:752px" role="img" aria-label="Video still of parents playing with their children"><div class="video-play"></div><div class="video-bar"></div></div>
<div class="abs video photo" style="left:554px;top:857px" role="img" aria-label="Video still of a family on the lawn by their home"><div class="video-play"></div><div class="video-bar"></div></div>

<footer class="abs footer"></footer>
<div class="abs fcol" style="left:119px"><h4>About Us</h4><ul><li>Company Info</li><li>Our Services</li><li>Clients</li><li>Partners</li></ul></div>
<div class="abs fcol" style="left:218px"><h4>Advice</h4><ul><li>Sign up</li><li>Forums</li><li>Promotion</li><li>Career</li></ul></div>
<div class="abs fcol" style="left:303px"><h4>Join In</h4><ul><li>FAQs</li><li>Solutions</li><li>Sitemap</li><li>Contacts</li></ul></div>
<div class="abs newsletter">Join our Newsletter</div>
<div class="abs nl-input">Email Address:</div>
<div class="abs nl-btn">Subscribe</div>
<div class="abs social" style="left:642px"></div>
<div class="abs social" style="left:665px"></div>
<div class="abs social" style="left:688px"></div>
<div class="abs divider"></div>
<div class="abs legal">Disclaimer &amp; Terms &amp; Conditions &nbsp;| &nbsp;Privacy Policy &nbsp;| Advertise With Us &nbsp;| &nbsp;Contact Us</div>
<div class="abs copy">Harbor Mortgage Relief &nbsp;© 2012. &nbsp;All Rights Reserved</div>
</body>
</html>
```